Business Cards + Flyer + Letterhead for Care Recruitment Agency

We are a recruitment agency for the health & care sector. We need designs made for business cards, A5 double-sided flyer, and a letterhead template.

Our branding message is professionalism, care, compassion, expertise. We are experts in recruitment for the care & health industry.

Our logo source files and colours are here - https://www.fileporta.net/sh/qrvn82lopx4kdte/BBBgKy8LMQ27uTnPwZxHcVobsa?dl=0

For the business card, I have attached an example we like. We want a vertical business card design, something very similar to the example given. The design should match our logo in terms of brand colors. On one side should be our logo, our website (www.hollowmere.co.uk) and Care Recruitment Specialists written somewhere visible that fits, between our logo and the website at the bottom. On the other side should be our details.

Details on the front:

Logo with slogan
Care Recruitment Specialists
www.hollowmere.co.uk

Details on the back:

Tobias Orlund
Managing Director

Pellam House, 31-39 Larkfield St, Birmingham, B4 7QD
07612 495371
tobias@hollowmere.co.uk
www.hollowmere.co.uk

Marnie Holloway
Business Development Director

07831 204968
marnie@hollowmere.co.uk
www.hollowmere.co.uk

For the A5 flyer, I have attached some pictures we've used for the website, which could be used for the flyer as well. To get a better idea of our branding, please visit our website - https://hollowmere.co.uk/

The text for the flyer is also attached.

Finally, the letterhead template should be a docx template with our logo and our identifiable branding (the same shapes and matching colours you will come up with for the business cards and flyer).

```html
<!DOCTYPE html>
<html lang="en">
<head>
<meta charset="utf-8">
<title>Hollowmere – Stationery Set</title>
<link rel="stylesheet" href="https://fonts.googleapis.com/css2?family=Jost:wght@400&family=Montserrat:wght@700&family=Lato:wght@300;700&family=Source+Sans+3:wght@400&display=swap">
<style>
:root{
  --navy:#1f3a73;
  --blue:#1a9ad9;
  --blue-deep:#0a7fc7;
  --ink-dark:#262a4a;
  --slate:#3e5185;
  --body-grey:#9a9ca3;
  --paper:#ffffff;
  --bg:#e9e9eb;
}
*{margin:0;padding:0;box-sizing:border-box}
html,body{width:1200px;height:1200px;overflow:hidden}
body{background:linear-gradient(160deg,#f8f8f9 0%,var(--bg) 100%);position:relative;font-family:"Source Sans 3",sans-serif}

/* Letterhead */
.letterhead{position:absolute;left:30px;top:149px;width:604px;height:804px;background:linear-gradient(#fff 0,#f1f1f3 268px,#fafafb 268px,#f2f2f4 100%);box-shadow:0 6px 18px rgba(0,0,0,.18);overflow:hidden}
.letterhead .waves{position:absolute;left:0;top:0}
.brand-block{position:absolute;left:20px;width:214px;top:80px;text-align:center}
.brand-mark{width:56px;height:56px;border-radius:50%;background:var(--blue);margin:0 auto 22px}
.brand-name{font-family:"Montserrat",sans-serif;font-weight:700;color:var(--navy);font-size:18px;letter-spacing:3px}
.lh-contacts{position:absolute;right:54px;top:42px;list-style:none}
.lh-contacts li{display:flex;align-items:center;justify-content:flex-end;gap:10px;color:var(--blue-deep);font-size:9.5px;line-height:11.5px;text-align:right;min-height:23px}
.lh-contacts .dot{width:19px;height:19px;border-radius:50%;background:var(--blue);flex:none;display:flex;align-items:center;justify-content:center}
.letter-body{position:absolute;left:38px;top:290px;width:509px;font-family:"Jost",sans-serif;font-size:12.4px;line-height:17.9px;color:var(--body-grey);text-align:justify;letter-spacing:.2px}
.letter-body p{margin-bottom:18px}
.signature{position:absolute;left:358px;top:618px;width:166px;height:48px;background:linear-gradient(90deg,rgba(40,40,50,.08),rgba(40,40,50,.03));border-radius:4px}
.signatory{position:absolute;left:358px;top:684px;font-size:8.5px;color:#b7b8bd}

/* Cards */
.card{position:absolute;width:229px;height:405px;border-radius:14px;overflow:hidden;box-shadow:-8px 6px 16px rgba(0,0,0,.22);background:#fff}
.card svg.bg{position:absolute;left:0;top:0}
.card-front{left:679px;top:73px}
.card-back-a{left:946px;top:175px}
.card-back-b{left:691px;top:533px}
.front-brand{position:absolute;left:0;right:0;top:110px;text-align:center}
.front-brand .brand-mark{width:52px;height:52px;margin-bottom:16px}
.front-brand .brand-name{font-size:17px;letter-spacing:2.6px}
.tagline{margin-top:6px;font-size:11px;color:var(--blue-deep)}
.front-web{position:absolute;left:0;right:0;top:358px;text-align:center;color:var(--blue);font-size:15px;font-weight:400}
.person{position:absolute;left:0;right:0;text-align:center}
.person-name{font-family:"Lato",sans-serif;font-size:21px;color:var(--navy);font-weight:300;letter-spacing:.3px}
.person-name b{font-weight:700}
.person-role{font-size:11px;color:var(--blue-deep);margin-top:2px}
.card-back-a .person{top:98px}
.card-back-b .person{top:98px}
.details{position:absolute;left:24px;list-style:none}
.card-back-a .details{top:243px}
.card-back-b .details{top:243px}
.details li{display:flex;align-items:center;gap:10px;height:38px;color:#fff;font-size:9.6px;line-height:12px}
.details .ring{width:30px;height:30px;border-radius:50%;border:1.5px solid var(--blue);flex:none;display:flex;align-items:center;justify-content:center}
</style>
</head>
<body>

<section class="letterhead">
  <svg class="waves" width="604" height="804" viewBox="0 0 604 804">
    <path d="M0 632 C130 740 300 800 430 770 L604 717 V804 H0Z" fill="var(--blue)"/>
    <path d="M0 690 C160 780 330 800 604 740 V804 H0Z" fill="var(--blue-deep)"/>
    <path d="M0 740 C140 790 300 804 420 804 H0Z" fill="var(--slate)" opacity=".5"/>
    <path d="M240 804 C360 760 470 735 604 717 V804Z" fill="var(--navy)"/>
    <path d="M380 804 C460 775 530 760 604 755 V804Z" fill="var(--ink-dark)"/>
  </svg>
  <div class="brand-block">
    <div class="brand-mark"></div>
    <div class="brand-name">HOLLOWMERE</div>
  </div>
  <ul class="lh-contacts">
    <li><span>Pellam House, 31-39 Larkfield St,<br>Birmingham, B4 7QD</span><span class="dot"><svg width="10" height="10" viewBox="0 0 10 10"><path d="M5 1a3 3 0 0 1 3 3c0 2-3 5-3 5S2 6 2 4a3 3 0 0 1 3-3z" fill="none" stroke="#fff" stroke-width="1.2"/><circle cx="5" cy="4" r="1" fill="#fff"/></svg></span></li>
    <li><span>0121 7612 495371</span><span class="dot"><svg width="10" height="10" viewBox="0 0 10 10"><path d="M2 1.5l2 .3.6 1.8-1 .8a6 6 0 0 0 2.2 2.2l.8-1 1.8.6.3 2c-4 .5-7.2-2.7-6.7-6.7z" fill="none" stroke="#fff" stroke-width="1"/></svg></span></li>
    <li><span>tobias@hollowmere.co.uk</span><span class="dot"><svg width="10" height="10" viewBox="0 0 10 10"><rect x="1" y="2.5" width="8" height="5.5" fill="none" stroke="#fff" stroke-width="1"/><path d="M1 2.5l4 3 4-3" fill="none" stroke="#fff" stroke-width="1"/></svg></span></li>
    <li><span>www.hollowmere.co.uk</span><span class="dot"><svg width="10" height="10" viewBox="0 0 10 10"><circle cx="5" cy="5" r="3.8" fill="none" stroke="#fff" stroke-width="1"/><ellipse cx="5" cy="5" rx="1.6" ry="3.8" fill="none" stroke="#fff" stroke-width=".8"/><path d="M1.2 5h7.6" stroke="#fff" stroke-width=".8"/></svg></span></li>
  </ul>
  <div class="letter-body">
    <p>Lorem ipsum dolor sit amet, consectetur adipiscing elit. Fusce dignissim pretium consectetur. Curabitur tempor posuere massa in varius. Pellentesque viverra nibh eu vehicula mattis. Nullam porta facilisis justo, a feugiat dolor sodales sed. Vestibulum neque nisi, elementum tincidunt metus sit amet, egestas bibendum enim. Aenean a blandit elit, vel rutrum mi. Nunc dapibus turpis sed massa aliquet tincidunt.</p>
    <p>Pellentesque id neque ligula. Nullam posuere, ligula a mattis posuere, lacus nisl adipiscing nunc, eu congue justo est ut diam. Nam quam nibh, dignissim non consequat in, semper eget purus. Nulla arcu sapien, viverra vitae metus tempor, congue ornare diam.</p>
    <p>Pellentesque vel nibh tempus, ullamcorper tortor sed, bibendum augue. Phasellus sollicitudin justo et quam aliquam sollicitudin. Sed eget nibh mollis, mattis sem et, viverra nulla.</p>
    <p>Pellentesque vel nibh tempus, ullamcorper tortor sed, bibendum augue. Phasellus sollicitudin justo et quam aliquam sollicitudin. Sed eget nibh mollis, mattis sem et, viverra nulla.</p>
  </div>
  <div class="signature" role="img" aria-label="Handwritten signature of the managing director"></div>
  <div class="signatory">MR. TOBIAS ORLUND</div>
</section>

<section class="card card-front">
  <svg class="bg" width="229" height="405" viewBox="0 0 229 405">
    <defs><linearGradient id="navyFront" x1="0" y1="0" x2="1" y2="1"><stop offset="0" stop-color="#2b2f55"/><stop offset="1" stop-color="#3a4f86"/></linearGradient></defs>
    <rect width="229" height="405" fill="url(#navyFront)"/>
    <path d="M0 330 L120 405 H0Z" fill="#4a5c91" opacity=".5"/>
    <path d="M0 206 C20 280 60 330 120 330 C170 325 200 290 229 270 V250 C180 280 150 307 110 307 C60 305 20 260 0 206Z" fill="var(--blue-deep)"/>
    <path d="M0 230 C30 300 70 325 110 322 C150 320 190 295 229 260 V250 C180 280 150 307 110 307 C60 305 20 260 0 206Z" fill="var(--blue)"/>
    <path d="M0 0 H229 V250 C180 280 150 307 110 307 C60 305 20 260 0 206Z" fill="#fff"/>
  </svg>
  <div class="front-brand">
    <div class="brand-mark"></div>
    <div class="brand-name">HOLLOWMERE</div>
    <div class="tagline">• Care Recruitment Specialists •</div>
  </div>
  <div class="front-web">www.hollowmere.co.uk</div>
</section>

<section class="card card-back-a">
  <svg class="bg" width="229" height="405" viewBox="0 0 229 405">
    <defs><linearGradient id="navyA" x1="0" y1="0" x2="1" y2="1"><stop offset="0" stop-color="#262a4a"/><stop offset="1" stop-color="#44588f"/></linearGradient></defs>
    <rect width="229" height="405" fill="url(#navyA)"/>
    <path d="M0 240 L90 405 H0Z" fill="#1f2545" opacity=".35"/>
    <path d="M0 164 C50 196 90 232 130 236 C180 236 210 200 229 168 V117 C200 190 160 222 120 218 C90 215 50 190 0 164Z" fill="var(--blue-deep)"/>
    <path d="M70 200 C100 225 130 236 160 230 C190 220 210 195 229 160 V117 C200 190 160 222 120 218Z" fill="var(--blue)"/>
    <path d="M0 0 H229 V117 C200 190 160 222 120 218 C90 215 50 190 0 164Z" fill="#fff"/>
  </svg>
  <div class="person">
    <div class="person-name">TOBIAS <b>ORLUND</b></div>
    <div class="person-role">MANAGING DIRECTOR</div>
  </div>
  <ul class="details">
    <li><span class="ring"><svg width="14" height="14" viewBox="0 0 14 14"><path d="M2 7L7 2.5 12 7M3.5 6v5.5h7V6" fill="none" stroke="#1a9ad9" stroke-width="1.1"/></svg></span><span>Pellam House, 31-39 Larkfield St,<br>Birmingham, B4 7QD</span></li>
    <li><span class="ring"><svg width="14" height="14" viewBox="0 0 14 14"><path d="M3 2l2.5.4.8 2.3-1.3 1a8 8 0 0 0 3 3l1-1.3 2.3.8.4 2.5C6 11.5 2.5 8 3 2z" fill="none" stroke="#1a9ad9" stroke-width="1.1"/></svg></span><span>0121 7612 495371</span></li>
    <li><span class="ring"><svg width="14" height="14" viewBox="0 0 14 14"><rect x="2" y="3.5" width="10" height="7" fill="none" stroke="#1a9ad9" stroke-width="1.1"/><path d="M2 3.5l5 4 5-4" fill="none" stroke="#1a9ad9" stroke-width="1.1"/></svg></span><span>tobias@hollowmere.co.uk</span></li>
    <li><span class="ring"><svg width="14" height="14" viewBox="0 0 14 14"><circle cx="7" cy="7" r="5" fill="none" stroke="#1a9ad9" stroke-width="1.1"/><ellipse cx="7" cy="7" rx="2" ry="5" fill="none" stroke="#1a9ad9"/><path d="M2 7h10" stroke="#1a9ad9"/></svg></span><span>www.hollowmere.co.uk</span></li>
  </ul>
</section>

<section class="card card-back-b">
  <svg class="bg" width="229" height="405" viewBox="0 0 229 405">
    <defs><linearGradient id="navyB" x1="0" y1="0" x2="1" y2="1"><stop offset="0" stop-color="#262a4a"/><stop offset="1" stop-color="#44588f"/></linearGradient></defs>
    <rect width="229" height="405" fill="url(#navyB)"/>
    <path d="M0 240 L90 405 H0Z" fill="#1f2545" opacity=".35"/>
    <path d="M0 164 C50 196 90 232 130 236 C180 236 210 200 229 168 V117 C200 190 160 222 120 218 C90 215 50 190 0 164Z" fill="var(--blue-deep)"/>
    <path d="M70 200 C100 225 130 236 160 230 C190 220 210 195 229 160 V117 C200 190 160 222 120 218Z" fill="var(--blue)"/>
    <path d="M0 0 H229 V117 C200 190 160 222 120 218 C90 215 50 190 0 164Z" fill="#fff"/>
  </svg>
  <div class="person">
    <div class="person-name">MARNIE <b>HOLLOWAY</b></div>
    <div class="person-role">BUSINESS DEVELOPMENT DIRECTOR</div>
  </div>
  <ul class="details">
    <li><span class="ring"><svg width="14" height="14" viewBox="0 0 14 14"><path d="M2 7L7 2.5 12 7M3.5 6v5.5h7V6" fill="none" stroke="#1a9ad9" stroke-width="1.1"/></svg></span><span>Pellam House, 31-39 Larkfield St,<br>Birmingham, B4 7QD</span></li>
    <li><span class="ring"><svg width="14" height="14" viewBox="0 0 14 14"><path d="M3 2l2.5.4.8 2.3-1.3 1a8 8 0 0 0 3 3l1-1.3 2.3.8.4 2.5C6 11.5 2.5 8 3 2z" fill="none" stroke="#1a9ad9" stroke-width="1.1"/></svg></span><span>0121 07831 204968</span></li>
    <li><span class="ring"><svg width="14" height="14" viewBox="0 0 14 14"><rect x="2" y="3.5" width="10" height="7" fill="none" stroke="#1a9ad9" stroke-width="1.1"/><path d="M2 3.5l5 4 5-4" fill="none" stroke="#1a9ad9" stroke-width="1.1"/></svg></span><span>marnie@hollowmere.co.uk</span></li>
    <li><span class="ring"><svg width="14" height="14" viewBox="0 0 14 14"><circle cx="7" cy="7" r="5" fill="none" stroke="#1a9ad9" stroke-width="1.1"/><ellipse cx="7" cy="7" rx="2" ry="5" fill="none" stroke="#1a9ad9"/><path d="M2 7h10" stroke="#1a9ad9"/></svg></span><span>www.hollowmere.co.uk</span></li>
  </ul>
</section>

</body>
</html>
```